Book cover for "Generous Horizons" encouraging business to take up compassion pr...

I need a book cover designed for "Generous Horizons. Where Winning Falls Short." The book encourages businesses to take up a social mission (that is, to have a social impact, such as corporate social responsibility.) in doing so, they find a greater sense of purpose, their employees and the community are more engaged, and their business grows. I use stories from my podcast Civic Purpose Uprising. 2 key word/phrases that may help t think about are Philanthropy and Corporate Social Responsibility.
This book will be followed by 1 or 2 other books. Another seies of books will also soon requre work.

The market is Mid-sized business owners and CEOs. They have built up the business to a successful place but now find that doesn't bring fulfilment or happiness. The cover needs to have a business or corporate feel.
The Colouring of the book, focus on blues and purples.
This will be a thin book - a quick and easy read of around 110 pages. It is 5x8 inches.
I would be happy to have a photo of me incorporated, but not the focus. I could have a photo done as directed by the designer, as I am planning to have a photoshoot done soon.
Fonts - Please chose a font with the rounded "a", such as in the Century Gothic font, however, open to suggestions.
The back cover will include:
o A book blurb – still to be written
o 2 or 3 endorsements
o Publishing logo (as it is my own publishing company.
o ISBN and barcode
On the spine
• Generous Horizons
• Belinda Morcombe
• Publisher logo icon

For your interest: Belinda is a Speaker, Author, podcaster and Trusted Advisor to Authentic Influencers. Through nourishing community, Belinda maximises the potential of business and influences change.

Target Market(s)

The market is Mid-sized business owners and CEOs. They have built up the business to a successful place but now find that doesn't bring fulfillment or happiness. The cover needs to have a business or corporate feel.

Industry/Entity Type

This is business/corporate book

Font styles to use
Other font styles liked:
• Please chose a font with the rounded "a", such as in the Century Gothic font, however, open to suggestions.

Colors
0054AA
0677BA
7BADD7
CADEEF
E8F1F8
A7469A
B969AE
D3A5CF
EDDBEB
F8F0F9
6B429C
8869AF
B7A5CE
E3DAEB
F3F0F8

Requirements
Must have
• An eye catching design with a business feel.
Nice to have
• I would be nice to edit me into the cover somehow - like Lindqvist puts himself in the background of his movies. I can have photos taken to match .

```html
<!DOCTYPE html>
<html lang="en">
<head>
<meta charset="utf-8">
<title>Generous Horizons — Book Cover</title>
<link href="https://fonts.googleapis.com/css2?family=Montserrat:wght@300;400;700&display=swap" rel="stylesheet">
<style>
  :root {
    --page-bg: #ececec;
    --cover-white: #ffffff;
    --title-magenta: #a51a77;
    --band-blue-dark: #005592;
    --band-blue: #0677ba;
    --portrait-plum: #6b2455;
    --portrait-light: #e4dde0;
    --portrait-mid: #b89aa9;
    --author-white: #ffffff;
  }
  * { margin: 0; padding: 0; box-sizing: border-box; }
  html, body {
    width: 1200px;
    height: 1200px;
    overflow: hidden;
    background: var(--page-bg);
  }
  .canvas {
    position: relative;
    width: 1200px;
    height: 1200px;
    display: flex;
    align-items: center;
    justify-content: center;
  }
  .book-cover {
    width: 728px;
    height: 1105px;
    box-shadow: 0 6px 24px rgba(0,0,0,0.12);
    background: var(--cover-white);
    overflow: hidden;
  }
  .book-cover svg { display: block; width: 100%; height: 100%; }
  .title-bold {
    font-family: "Montserrat", sans-serif;
    font-weight: 700;
    font-size: 142px;
    fill: var(--title-magenta);
    letter-spacing: -2px;
  }
  .title-light {
    font-family: "Montserrat", sans-serif;
    font-weight: 300;
    font-size: 176px;
    fill: var(--title-magenta);
    letter-spacing: -2px;
  }
  .subtitle {
    font-family: "Montserrat", sans-serif;
    font-weight: 400;
    font-size: 42px;
    fill: var(--title-magenta);
  }
  .author-name {
    font-family: "Montserrat", sans-serif;
    font-weight: 400;
    font-size: 38px;
    fill: var(--author-white);
    letter-spacing: 1px;
  }
</style>
</head>
<body>
<main class="canvas">
  <section class="book-cover">
    <svg viewBox="0 0 870 1320" xmlns="http://www.w3.org/2000/svg">
      <defs>
        <linearGradient id="bandGradient" x1="0" y1="0" x2="1" y2="0">
          <stop offset="0" stop-color="var(--band-blue-dark)"/>
          <stop offset="1" stop-color="var(--band-blue)"/>
        </linearGradient>
        <linearGradient id="portraitGradient" x1="0" y1="0" x2="0" y2="1">
          <stop offset="0" stop-color="var(--portrait-light)"/>
          <stop offset="0.3" stop-color="var(--portrait-mid)"/>
          <stop offset="0.5" stop-color="var(--portrait-plum)"/>
          <stop offset="1" stop-color="var(--portrait-plum)"/>
        </linearGradient>
      </defs>

      <rect class="cover-ground" width="870" height="1320" fill="var(--cover-white)"/>

      <path class="author-portrait" role="img" aria-label="Photo of the author, smiling, arms folded, in a plum sleeveless dress"
            d="M470 1320 L470 460 Q470 335 595 335 L870 335 L870 1320 Z"
            fill="url(#portraitGradient)"/>

      <text class="title-bold" transform="translate(220 1070) rotate(-90)">generous</text>
      <text class="title-light" transform="translate(378 1140) rotate(-90)">horizons</text>
      <text class="subtitle" transform="translate(458 785) rotate(-90)">Where Winning Falls Short</text>

      <polygon class="chevron-band" points="0,980 435,1195 870,1000 870,1200 435,1395 0,1175" fill="url(#bandGradient)"/>

      <text class="author-name" transform="translate(80 1110) rotate(27)">Belinda Morcombe</text>
    </svg>
  </section>
</main>
</body>
</html>
```